Business Card Design Project

WE NEED A CARD WITH THE NAME AND LOGO IN ONE SIDE AND THE ODER JUST THE INFORMATIONS LIKE NAME, E-MAIL, PHONE AND SITE. I HAVE A IDEA OF THE CARD ALL BLACK AND JUST COLLOORS IN THE LOGO AND INFORMATIONS. WE WANT SANTHING SIMPLE AND ELEGANT. SAMETHING NEW WICTH PASS CONFIANCE.
Updates

I HAVE UP DATE THE INFORMATIONS OF WAHT WE NEED. THNKSĀ 

Target Market(s)

COMPANY WHO ORGANIZE BIG CORPORATIVE EVENTS.

Industry/Entity Type

Business

Requirements
Should not have
• MUCH INFORMATION.

```html
<!DOCTYPE html>
<html lang="en">
<head>
<meta charset="utf-8">
<title>Velaro – Business Card</title>
<link href="https://fonts.googleapis.com/css2?family=Montserrat:wght@400;500;600&display=swap" rel="stylesheet">
<style>
  :root {
    --backdrop: #3a3a3a;
    --card: #050505;
    --orange: #f06a2a;
    --gold: #f5a524;
    --white: #f2f2f2;
    --muted: #bdbdbd;
  }
  * { box-sizing: border-box; margin: 0; padding: 0; }
  html, body { width: 1200px; height: 900px; overflow: hidden; }
  body {
    background: var(--backdrop);
    font-family: "Montserrat", sans-serif;
    display: flex;
    align-items: center;
    justify-content: center;
    gap: 40px;
  }
  .card {
    width: 520px;
    height: 300px;
    background: var(--card);
    border-radius: 70px 4px 70px 4px;
    position: relative;
    box-shadow: 0 12px 30px rgba(0,0,0,.45);
    overflow: hidden;
  }

  /* front */
  .card-front {
    display: flex;
    flex-direction: column;
    align-items: center;
    justify-content: center;
    gap: 10px;
  }
  .brand-name {
    color: var(--orange);
    font-size: 44px;
    font-weight: 500;
    line-height: 1;
    letter-spacing: 1px;
  }
  .brand-line {
    color: var(--muted);
    font-size: 14px;
    font-weight: 400;
    letter-spacing: 3px;
  }

  /* back */
  .back-brand {
    position: absolute;
    left: 60px;
    top: 60px;
    color: var(--orange);
    font-size: 30px;
    font-weight: 500;
    letter-spacing: 1px;
  }
  .contact {
    position: absolute;
    left: 250px;
    top: 118px;
  }
  .person-name {
    color: var(--gold);
    font-size: 23px;
    font-weight: 500;
    line-height: 1.1;
  }
  .person-role {
    color: var(--orange);
    font-size: 16px;
    font-weight: 400;
    margin-bottom: 14px;
  }
  .contact-list { list-style: none; }
  .contact-item {
    display: flex;
    align-items: center;
    gap: 10px;
    color: var(--white);
    font-size: 14px;
    height: 26px;
    white-space: nowrap;
  }
  .contact-icon { width: 20px; height: 20px; flex: none; }
</style>
</head>
<body>
  <section class="card card-front">
    <p class="brand-name">Velaro</p>
    <p class="brand-line">Audiovisual e Cenografia</p>
  </section>

  <section class="card card-back">
    <p class="back-brand">Velaro</p>
    <div class="contact">
      <p class="person-name">Example Name</p>
      <p class="person-role">Position</p>
      <ul class="contact-list">
        <li class="contact-item">
          <svg class="contact-icon" viewBox="0 0 20 20" fill="none" stroke="#f5a524" stroke-width="1.4"><circle cx="10" cy="10" r="9"/><rect x="7" y="5" width="6" height="10" rx="1"/></svg>
          123 456 789
        </li>
        <li class="contact-item">
          <svg class="contact-icon" viewBox="0 0 20 20" fill="none" stroke="#f5a524" stroke-width="1.4"><circle cx="10" cy="10" r="9"/><circle cx="10" cy="10" r="5"/><path d="M5 10h10M10 5c-2 3-2 7 0 10M10 5c2 3 2 7 0 10"/></svg>
          www.yoursite.com
        </li>
        <li class="contact-item">
          <svg class="contact-icon" viewBox="0 0 20 20" fill="none" stroke="#f5a524" stroke-width="1.4"><circle cx="10" cy="10" r="9"/><rect x="5" y="6.5" width="10" height="7"/><path d="M5 6.5l5 4 5-4"/></svg>
          info@yoursite.com
        </li>
        <li class="contact-item">
          <svg class="contact-icon" viewBox="0 0 20 20" fill="none" stroke="#f5a524" stroke-width="1.4"><circle cx="10" cy="10" r="9"/><path d="M10 15s-3.5-3.5-3.5-6a3.5 3.5 0 0 1 7 0c0 2.5-3.5 6-3.5 6z"/><circle cx="10" cy="9" r="1"/></svg>
          Address Line here 1234
        </li>
      </ul>
    </div>
  </section>
</body>
</html>
```